Real Estate Business Folders, Business Cards, Envelopes & Letterhead

Im looking for trendy, modern & professional design concepts for my business folder that will be used for real estate documents and property report presentations. I'm also looking for Business card designs, envelopes and letterhead with a similar theme. I have a logo already and I would like the logo colors to be incorporated in the design concepts.

Target Market(s)

Real Estate Investors, Banks, Financial Institutions

Industry/Entity Type

Real Estate

Colors
0455a3
959595
d3d3d3
848484

Requirements
Must have
• Trendy Modern, High Class look. Please include logo and colors and incorporate some silver or metallic.
• Business Address: 4127 Corvello Blvd ste 208-310
• Corvello Springs, NV 89190
• Phone: 702-555-0187
• Fax : 702-555-0142
• Email: info@brookmerecastlesales.example
• Website: BrookmereCastleSales.example

```html
<!DOCTYPE html>
<html lang="en">
<head>
<meta charset="utf-8">
<title>Brookmere Castle Sales – Business Card</title>
<link rel="stylesheet" href="https://fonts.googleapis.com/css2?family=Open+Sans:wght@400;600;700&display=swap">
<style>
  :root {
    --brand-blue: #0455a3;
    --mid-grey: #848484;
    --soft-grey: #959595;
    --light-grey: #d3d3d3;
    --ink: #3a3a3a;
    --paper: #ffffff;
    --stage: #2b2b2d;
  }
  * { box-sizing: border-box; margin: 0; padding: 0; }
  html, body { width: 1200px; height: 885px; overflow: hidden; }
  body {
    background: var(--stage);
    font-family: "Open Sans", Arial, sans-serif;
    position: relative;
  }
  .card {
    position: absolute;
    width: 560px;
    height: 320px;
    border-radius: 2px;
    box-shadow: 0 10px 30px rgba(0,0,0,.45);
    overflow: hidden;
  }
  /* Back side */
  .card-back {
    left: 80px; top: 90px;
    background: linear-gradient(135deg, #f4f4f4 0%, #dcdcdc 35%, #f7f7f7 60%, #c9c9c9 100%);
    display: flex; flex-direction: column; align-items: center; justify-content: center;
  }
  .back-name {
    font-size: 30px; font-weight: 600; color: var(--ink);
    letter-spacing: .5px;
  }
  .back-web {
    margin-top: 70px; font-size: 15px; color: var(--ink);
  }
  /* Front side */
  .card-front {
    left: 560px; top: 475px;
    background: var(--paper);
  }
  .edge-strip {
    position: absolute; left: 0; top: 0; bottom: 0; width: 26px;
    background: var(--brand-blue);
  }
  .edge-strip span {
    position: absolute; left: 8px; width: 10px; height: 10px; background: var(--paper);
  }
  .brand {
    position: absolute; right: 32px; top: 40px;
    display: flex; align-items: center; gap: 10px;
    font-size: 24px; font-weight: 600; color: var(--brand-blue);
  }
  .brand-square { width: 18px; height: 18px; background: var(--brand-blue); }
  .divider { position: absolute; height: 1px; background: var(--mid-grey); }
  .divider-top { left: 210px; right: 32px; top: 96px; }
  .divider-bottom { left: 56px; right: 300px; top: 222px; }
  .address {
    position: absolute; right: 32px; top: 110px; text-align: right;
    font-size: 14px; line-height: 1.45; color: var(--ink); font-style: normal;
  }
  .address .web { margin-top: 8px; }
  .person { position: absolute; left: 56px; top: 166px; }
  .person-name { font-size: 22px; font-weight: 700; color: var(--brand-blue); line-height: 1.1; }
  .person-title { font-size: 15px; color: var(--soft-grey); }
  .contacts {
    position: absolute; left: 56px; top: 234px; list-style: none;
    font-size: 15px; color: var(--ink); line-height: 1.45;
  }
  .contacts li { display: flex; align-items: center; gap: 10px; }
  .contacts svg { width: 14px; height: 14px; fill: var(--brand-blue); flex: none; }
</style>
</head>
<body>
  <section class="card card-back" aria-label="Card back">
    <p class="back-name">Brookmere Castle Sales</p>
    <p class="back-web">www.BrookmereCastleSales.example</p>
  </section>

  <section class="card card-front" aria-label="Card front">
    <div class="edge-strip">
      <span style="top:18px"></span><span style="top:58px"></span><span style="top:98px"></span>
      <span style="top:138px"></span><span style="top:178px"></span><span style="top:218px"></span>
      <span style="top:258px"></span><span style="top:298px"></span>
    </div>

    <div class="brand"><span class="brand-square"></span>Brookmere Castle Sales</div>
    <div class="divider divider-top"></div>

    <address class="address">
      <p>4127 Corvello Blvd ste 208-310</p>
      <p>Corvello Springs, NV 89190</p>
      <p class="web">BrookmereCastleSales.example</p>
    </address>

    <div class="person">
      <p class="person-name">MARA LINDQVIST</p>
      <p class="person-title">PRESIDENT</p>
    </div>
    <div class="divider divider-bottom"></div>

    <ul class="contacts">
      <li><svg viewBox="0 0 16 16" aria-hidden="true"><path d="M3 1h3l1 4-2 1a9 9 0 0 0 5 5l1-2 4 1v3c0 1-1 2-2 2A13 13 0 0 1 1 3c0-1 1-2 2-2z"/></svg>702-555-0187</li>
      <li><svg viewBox="0 0 16 16" aria-hidden="true"><path d="M4 1h8v4H4zM1 6h14v7h-3v2H4v-2H1zM5 10v4h6v-4z"/></svg>702-555-0142</li>
      <li><svg viewBox="0 0 16 16" aria-hidden="true"><path d="M1 3h14v10H1zM2 4l6 5 6-5z" fill-rule="evenodd"/></svg>info@brookmerecastlesales.example</li>
    </ul>
  </section>
</body>
</html>
```